Fresh Dwelling Tract Hub needs a new Landing Page

I like to get a landing page or website with 2-3 pages to help target home buyers who are looking to buy homes from builders such as TQ Estates, Vostrum, P.J. Calloway, etc. The landing page/website to be non-cluttered and be able to explain to home buyers that there are many benefits to include me as their buyer's agent when they buy a brand new home from any builders.
I may want to incorporate a short explanation video (animated) on the landing page and then for the viewer to click on a button that will take them to another page where they can search for new homes from different builders.
Target Market(s)
Home buyers looking to buy brand new home from builders such as TQ Estates, Vostrum, P.J. Calloway, etc.
Industry/Entity Type
Real Estate
Number of Pages Required
2 page
Requirements
Must have
- The landing page may have the explanation video at the bottom of the landing page (scrolled down) or there may be a CALL TO ACTION button that takes the viewer to the 2nd page to watch the explanation video. Once they watched the explanation video and are still interested, they can click on another CALL TO ACTION button that will take them to another website that they will be able to search for all the available new homes and register their contact information.
Should not have
- No clutters and no dark colors.

```html
<!DOCTYPE html>
<html lang="en">
<head>
<meta charset="utf-8">
<title>Parkside Home Walk</title>
<link rel="stylesheet" href="https://fonts.googleapis.com/css2?family=Open+Sans:wght@400;600;700&family=Raleway:wght@500;600;700&display=swap">
<style>
:root{
  --yellow:#fcc419;
  --yellow-deep:#f3b500;
  --blue:#2f62a8;
  --ink:#2b2b2b;
  --text:#555;
  --muted:#8a8a8a;
  --line:#dcdcdc;
  --soft:#f3f3f3;
  --white:#fff;
  --footer:#262626;
  --footer-text:#9a9a9a;
}
*{box-sizing:border-box;margin:0;padding:0}
html,body{width:1200px;height:3372px;overflow:hidden}
body{font-family:"Open Sans",Arial,sans-serif;color:var(--text);background:var(--white);position:relative}
.section{position:absolute;left:0;width:1200px}
h2,h3,.brand{font-family:"Raleway",Arial,sans-serif;color:var(--ink)}
.btn{display:inline-block;font:700 13px "Open Sans",Arial,sans-serif;text-transform:uppercase;letter-spacing:.3px;padding:0 18px;line-height:30px;border-radius:2px;white-space:nowrap}
.btn-yellow{background:var(--yellow);color:var(--ink)}
.btn-blue{background:var(--blue);color:var(--white);line-height:32px;padding:0 38px}
.btn-outline{border:1px solid var(--blue);color:var(--blue);background:var(--white)}
.photo{border-radius:2px}

/* header */
.site-header{top:0;height:150px;border-bottom:1px solid var(--line)}
.site-header .brand{position:absolute;left:168px;top:32px;font-size:22px;font-weight:600;color:#6b4e2e;line-height:1.1}
.site-header .brand small{display:block;font-size:12px;letter-spacing:3px;text-transform:uppercase;color:var(--muted)}
.search{position:absolute;left:705px;top:36px;width:200px;height:32px;border:1px solid var(--line);border-radius:3px;font-size:10.5px;color:var(--muted);line-height:30px;padding-left:30px;white-space:nowrap;overflow:hidden}
.search svg{position:absolute;left:10px;top:8px}
.site-header .callback{position:absolute;left:915px;top:36px;line-height:32px}
.header-rule{position:absolute;left:0;top:105px;width:1200px;border-top:1px solid var(--line)}
.main-nav{position:absolute;top:118px;left:0;width:1200px;display:flex;justify-content:center}
.main-nav a{font-size:15px;color:var(--ink);text-decoration:none;width:150px;text-align:center;white-space:nowrap}

/* hero */
.hero{top:150px;height:460px;overflow:hidden;background:var(--yellow)}
.hero-shape{position:absolute;left:0;top:0}
.hero-person{position:absolute;left:110px;top:0;width:280px;height:460px;background:linear-gradient(180deg,#e9dcc8 0%,#d8b98d 40%,#e8c64a 100%)}
.hero-tree{position:absolute;right:20px;top:140px;width:230px;height:320px;background:radial-gradient(ellipse at 50% 55%,rgba(255,255,255,.55),rgba(255,255,255,0) 70%)}
.hero-brand{position:absolute;left:0;width:1200px;top:80px;text-align:center}
.hero-brand .mark{display:inline-block;width:34px;height:34px;border-radius:50%;background:var(--yellow-deep);vertical-align:middle;margin-right:10px}
.hero-brand .brand{font-size:36px;font-weight:600;color:#6b4e2e;vertical-align:middle}
.hero-copy{position:absolute;left:0;width:1200px;top:203px;text-align:center;font-size:16px;color:var(--ink);line-height:24px}
.hero-copy strong{font-weight:700}
.hero .btn-blue{position:absolute;left:512px;top:272px}

/* builders */
.builders{top:610px;height:345px;background:var(--soft)}
.builders h2{position:absolute;left:180px;top:90px;font-size:24px;font-weight:600;line-height:30px}
.builders p{position:absolute;left:180px;top:172px;width:400px;font-size:13px;line-height:21px}
.builder-list{position:absolute;left:650px;top:125px;width:400px}
.builder{position:absolute;font-family:"Open Sans",Arial,sans-serif;font-weight:700;color:var(--ink);white-space:nowrap}
.builder-tq{left:95px;top:0;background:var(--white);border:1px solid var(--line);padding:6px 16px;font-size:24px}
.builder-pj{left:0;top:80px;font-size:22px}
.builder-vo{left:200px;top:80px;font-size:22px}
.builder-pj::before,.builder-vo::before{content:"";display:inline-block;width:14px;height:14px;background:var(--ink);margin-right:8px;vertical-align:middle}

/* steps */
.steps{top:955px;height:930px}
.steps h2{position:absolute;top:68px;width:1200px;text-align:center;font-size:28px;font-weight:600}
.steps .lead{position:absolute;top:112px;width:1200px;text-align:center;font-size:14px}
.step{position:absolute;width:435px;height:190px;border:1px solid var(--line);background:var(--white);box-shadow:0 2px 4px rgba(0,0,0,.05)}
.step .num{position:absolute;left:-28px;top:66px;width:56px;height:56px;border-radius:50%;background:var(--white);border:1px solid var(--line);font:300 30px "Raleway",Arial,sans-serif;color:var(--muted);text-align:center;line-height:54px}
.step h3{position:absolute;left:45px;top:32px;width:200px;font:700 13px/19px "Open Sans",Arial,sans-serif;color:var(--ink)}
.step p{position:absolute;left:45px;top:58px;width:200px;font-size:13px;line-height:21px}
.step .photo{position:absolute;right:0;top:0;width:180px;height:188px}
.step-1{left:140px;top:180px}
.step-2{left:640px;top:180px;width:350px}
.step-3{left:400px;top:412px;width:435px}
.step-4{left:140px;top:645px}
.step-5{left:640px;top:645px;width:350px}
.step-5 h3{top:22px;width:160px}
.step-5 p{top:64px;width:180px;line-height:20px}
.step-2 p{width:180px}

/* testimonial */
.testimonial{top:1885px;height:415px;background:var(--soft)}
.testimonial .avatar{position:absolute;left:297px;top:40px;width:240px;height:240px;border-radius:50%;border:5px solid var(--white);background:radial-gradient(circle at 50% 40%,#e9c9a6,#b98f6a 70%,#8fb0c4)}
.stat{position:absolute;left:297px;width:240px;text-align:center;color:var(--blue);font-size:15px}
.stat strong{font-weight:700;font-size:20px}
.testimonial .quote-mark{position:absolute;left:632px;top:80px;font:700 40px Georgia,serif;color:var(--yellow)}
.testimonial blockquote{position:absolute;left:660px;top:95px;width:360px;font-size:16px;line-height:25px;color:var(--text)}
.testimonial .who{position:absolute;left:660px;top:222px;font-size:13px;color:var(--ink);font-weight:600}
.testimonial .who span{display:block;font-weight:400;color:var(--muted)}
.testimonial .btn{position:absolute;left:660px;top:275px;font-size:11px;line-height:28px}

/* about */
.about{top:2300px;height:410px}
.about h2{position:absolute;left:188px;top:55px;font-size:26px;font-weight:600}
.about p{position:absolute;left:188px;width:395px;font-size:13px;line-height:21px}
.about .btn{position:absolute;left:188px;top:335px;font-size:11px;line-height:28px}
.about .video{position:absolute;left:650px;top:95px;width:378px;height:222px;background:linear-gradient(160deg,#eef2f4 0%,#dfe6e8 55%,#a7c25c 100%)}
.play{position:absolute;left:172px;top:94px;width:36px;height:36px;border-radius:50%;background:var(--yellow)}
.play svg{position:absolute;left:13px;top:10px}

/* contact agent */
.agent{top:2710px;height:320px;background:var(--soft)}
.agent .tree{position:absolute;right:110px;top:20px;width:240px;height:300px;background:radial-gradient(ellipse at 50% 45%,rgba(0,0,0,.05),rgba(0,0,0,0) 70%)}
.agent h2{position:absolute;top:165px;width:1200px;text-align:center;font-size:26px;font-weight:600}
.agent p{position:absolute;top:213px;width:1200px;text-align:center;font-size:14px;color:var(--ink)}
.agent .btn{position:absolute;left:527px;top:244px;font-size:11px;line-height:28px}

/* footer */
.site-footer{top:3030px;height:342px;background:var(--footer);color:var(--footer-text);font-size:13px}
.site-footer .band{position:absolute;top:0;left:0;width:1200px;height:30px;background:#1f1f1f}
.foot-col{position:absolute;top:78px;list-style:none;line-height:30px}
.foot-col a{color:#cfcfcf;text-decoration:none}
.foot-col-1{left:148px}
.foot-col-2{left:310px}
.foot-note{position:absolute;left:490px;top:78px;width:520px;line-height:20px;font-size:12px;color:#6f6f6f}
.social{position:absolute;left:490px;top:160px;display:flex;align-items:center;gap:14px;color:#cfcfcf}
.social i{display:block;width:20px;height:20px;background:#8d8d8d;border-radius:50%}
.social i.sq{border-radius:3px}
.legal{position:absolute;left:490px;top:208px;font-size:12px}
.legal a{color:#6f6f6f;margin-right:40px}
.copyright{position:absolute;left:0;width:1200px;top:298px;text-align:center;font-size:10px;color:#6f6f6f;line-height:18px}
.copyright i{display:inline-block;width:10px;height:10px;background:#6f6f6f;vertical-align:middle;margin-right:6px}
</style>
</head>
<body>

<header class="section site-header">
  <div class="brand">Parkside <small>Home Walk</small></div>
  <div class="search"><svg width="14" height="14" viewBox="0 0 14 14"><circle cx="6" cy="6" r="4.5" fill="none" stroke="#999" stroke-width="1.5"/><line x1="9.5" y1="9.5" x2="13" y2="13" stroke="#999" stroke-width="1.5"/></svg>Search by City, Zip, or Address</div>
  <a class="btn btn-yellow callback">Request a callback</a>
  <div class="header-rule"></div>
  <nav class="main-nav">
    <a>Property search</a><a>Arrange a viewing</a><a>Fees</a><a>Reviews</a><a>About</a><a>Contact</a>
  </nav>
</header>

<section class="section hero">
  <svg class="hero-shape" width="1200" height="460" viewBox="0 0 1200 460">
    <path d="M0 0 H1200 V30 C1060 290 760 370 520 345 C330 320 190 200 120 60 L95 0 Z" fill="#fff"/>
  </svg>
  <div class="hero-person photo" role="img" aria-label="Smiling agent in a yellow jacket"></div>
  <div class="hero-tree" role="img" aria-label="White tree decoration"></div>
  <div class="hero-brand"><span class="mark"></span><span class="brand">Parkside Home Walk</span></div>
  <p class="hero-copy">Buy your home quickly for a low fixed fee and save over $8,000.<br><strong>Fixed fees from $950.</strong></p>
  <a class="btn btn-blue">Property search</a>
</section>

<section class="section builders">
  <h2>Your Interactive Guide<br>for All Things Home.</h2>
  <p>Dreaming your new home? We will help home buyers who are looking to buy homes from builders such as TQ Estates, Vostrum, P.J. Calloway, etc and helping you make the best buying &amp; financing decisions with start-to-finish advice and smart home tips.</p>
  <div class="builder-list">
    <span class="builder builder-tq">TQ Estates</span>
    <span class="builder builder-pj">P.J. Calloway</span>
    <span class="builder builder-vo">Vostrum</span>
  </div>
</section>

<section class="section steps">
  <h2>How it works</h2>
  <p class="lead">We help you win at every step of the home buying process.</p>

  <article class="step step-1">
    <span class="num">1</span>
    <h3>Head Start on New Listings</h3>
    <p>We update listings every 10 minutes on parksidewalk.com so you can see them first.</p>
    <div class="photo" role="img" aria-label="Hands holding a tablet" style="background:linear-gradient(135deg,#e8e4df,#b9b3ab)"></div>
  </article>

  <article class="step step-2">
    <span class="num">2</span>
    <h3>Meet With Your Agent</h3>
    <p>Your Agent will learn your needs to find you the right home and help you get loan pre approval.</p>
    <div class="photo" role="img" aria-label="Handshake with an agent" style="width:115px;background:linear-gradient(135deg,#d9c38a,#8a6a3f)"></div>
  </article>

  <article class="step step-3">
    <span class="num">3</span>
    <h3>Tour Homes, Even Same Day!</h3>
    <p style="width:190px">Book online and get in right away with your agent or a team member to stay ahead of other buyers.</p>
    <div class="photo" role="img" aria-label="Green front door of a house" style="background:linear-gradient(180deg,#f1e9e2,#9ec3b4 60%,#e7d9cc)"></div>
  </article>

  <article class="step step-4">
    <span class="num">4</span>
    <h3>Make an Offer Right for You</h3>
    <p>Our agents are paid based on your satisfaction, so they'll tell you when to walk away. Our focus is getting you the right home</p>
    <div class="photo" role="img" aria-label="Row of painted houses" style="background:linear-gradient(180deg,#7fb3de,#c9b8a8 55%,#6f7d63)"></div>
  </article>

  <article class="step step-5">
    <span class="num">5</span>
    <h3>Close Smoothly and Save Thousands!</h3>
    <p>Your agent will guide you through the closing process And we pay $2,000 on average toward your closing costs.</p>
    <div class="photo" role="img" aria-label="Happy couple at home" style="width:115px;background:linear-gradient(135deg,#f2ebe3,#d6a88a)"></div>
  </article>
</section>

<section class="section testimonial">
  <div class="avatar" role="img" aria-label="Couple portrait"></div>
  <p class="stat" style="top:318px">Bought in <strong>2</strong> days</p>
  <p class="stat" style="top:345px">Saved <strong>$6500</strong> in fees</p>
  <span class="quote-mark">“</span>
  <blockquote>Buying with Parkside Home Walk was a triple win: The web site was easy to use, The way we setup home tours was efficient, and we even got money back at the end.</blockquote>
  <p class="who">Lena and Marco<span>San Diego</span></p>
  <a class="btn btn-yellow">Read reviews</a>
</section>

<section class="section about">
  <h2>What is Parkside Home Walk?</h2>
  <p style="top:105px">Lorem ipsum dolor sit amet, consectetur adipiscing elit. Cras ultricies neque ut turpis molestuada, quis accumsan nisl ultricies. Aenean ultrices molestie tellus, id ultricies odio finibus non. Praesent faucibus neque nunc, vitae egestas turpis feugiat et.</p>
  <p style="top:215px">Curabitur rhoncus nec turpis at pellentesque. Sed eu congue nisi. Donec nec nisi tellus. Quisque consectetur elit sit amet ex consequat, eget dapibus neque varius. Quisque fermentum ex elit, quis elementum quam sagittis et.</p>
  <a class="btn btn-outline">See our story</a>
  <div class="video" role="img" aria-label="Animated explainer video of a family on a sofa">
    <span class="play"><svg width="12" height="16" viewBox="0 0 12 16"><path d="M0 0 L12 8 L0 16 Z" fill="#fff"/></svg></span>
  </div>
</section>

<section class="section agent">
  <div class="tree" role="img" aria-label="Faint tree decoration"></div>
  <h2>Meet With an Agent</h2>
  <p>A local Agent will help you find your dream home.</p>
  <a class="btn btn-yellow">Request a meeting</a>
</section>

<footer class="section site-footer">
  <div class="band"></div>
  <ul class="foot-col foot-col-1">
    <li><a>Property search</a></li><li><a>Arrange a viewing</a></li><li><a>Fees</a></li><li><a>Reviews</a></li>
  </ul>
  <ul class="foot-col foot-col-2">
    <li><a>Agent Support</a></li><li><a>Contact us</a></li>
  </ul>
  <p class="foot-note">If you are using a screen reader or having trouble reading this website, please call our Customer Support for help at 1 (800) 555-0142. Prices, conditions and home availability are subject to change without notice.</p>
  <div class="social">Connect with us: <i class="sq"></i><i class="sq"></i><i></i><i></i><i></i></div>
  <p class="legal"><a>Terms &amp; Conditions</a><a>Privacy Policy</a></p>
  <p class="copyright"><i></i>Equal Housing Opportunity<br>Parkside Home Walk © 2016 All Rights Reserved</p>
</footer>

</body>
</html>
```